Social Media Application Design - Android and IOS

I am ready to go live with new social media app however I am not comfortable with the current design. It is a not interactive or attractive enough. Please note the splash screen is a green, so preference would be to keep a green theme although I am more than happy to consider other colours that would improve the design.
The attachment has the app screens that need to be redesigned. They may not need massive changes , however keen to go live so looking for inspired designers to support with this project and many others that I have, including ongoing work on this app.
Target Market(s)
Millenials
Industry/Entity Type
Social
Colors
Designer to choose colors to be used in the design.
Requirements
Must have
- Please see attached document for screens that I would like redesigned. It needs to work with Android and IOS. I am looking for the design and not the functionality.
Nice to have
- Highly interactive design. Please see polling functionality of Pictavo.
Should not have
- should not be complicated - simplicity is the key

```html
<!DOCTYPE html>
<html lang="en">
<head>
<meta charset="utf-8">
<title>QUERO – App Screens</title>
<link href="https://fonts.googleapis.com/css2?family=Open+Sans:wght@400;600;700&display=swap" rel="stylesheet">
<style>
:root{
  --bg:#3f5b6d;
  --teal-a:#55dbc3;
  --teal-b:#3db6d8;
  --accent:#3cc3c9;
  --ink:#333c44;
  --muted:#9aa3aa;
  --line:#e8ecef;
  --field:#f6f8f9;
}
*{box-sizing:border-box;margin:0;padding:0}
html,body{width:1200px;height:1200px;overflow:hidden;background:var(--bg);font-family:"Open Sans",sans-serif;color:var(--ink)}
.screen{position:absolute;width:180px;height:320px;background:#fff;overflow:hidden}
.abs{position:absolute}
.bar{position:absolute;top:0;left:0;right:0;height:32px;background:linear-gradient(90deg,var(--teal-a),var(--teal-b));color:#fff}
.status{position:absolute;top:2px;left:5px;right:5px;height:8px;font-size:4.5px;display:flex;justify-content:space-between;align-items:center}
.status .batt{display:inline-block;width:10px;height:4px;background:#fff;border-radius:1px;vertical-align:middle;margin-left:2px}
.nav{position:absolute;top:12px;left:0;right:0;height:20px;display:flex;align-items:center;justify-content:space-between;padding:0 8px;font-size:7px;font-weight:600}
.nav .title{position:absolute;left:0;right:0;text-align:center;font-size:9px;font-weight:600;pointer-events:none}
.brand{font-weight:700;letter-spacing:.5px;font-size:9px}
.burger{width:10px;height:7px;border-top:1px solid #fff;border-bottom:1px solid #fff;position:relative}
.burger:after{content:"";position:absolute;left:0;right:0;top:2px;border-top:1px solid #fff}
.nav-icons{display:flex;gap:6px}
.back{font-size:10px;font-weight:400}
/* feed */
.post{position:absolute;left:10px;right:10px;height:120px}
.who{position:absolute;top:0;left:0;right:0;display:flex;align-items:center;font-size:5px;gap:3px}
.avatar{width:10px;height:10px;border-radius:50%;background:linear-gradient(135deg,#8a5a44,#d9a37c)}
.who .time{color:var(--muted);font-size:4px}
.who .ago{margin-left:auto;color:var(--muted);font-size:4px}
.q{position:absolute;top:19px;left:0;right:0;font-size:5.5px;display:flex;justify-content:space-between;align-items:center}
.votes{font-size:3.5px;color:var(--accent);border:.6px solid var(--accent);border-radius:4px;padding:0 3px}
.pics{position:absolute;top:28px;left:0;right:0;height:59px;display:flex;gap:5px}
.pic{flex:1;position:relative;color:#fff;font-size:4.5px;font-weight:600}
.pic .cap{position:absolute;left:3px;bottom:3px}
.ph-a{background:linear-gradient(135deg,#0e1a2a,#b02a2a 60%,#1d2c3c)}
.ph-b{background:linear-gradient(135deg,#2b2a33,#6d6c78 55%,#1e1d24)}
.ph-c{background:linear-gradient(135deg,#2f3640,#7b6a5c 60%,#2c3a47)}
.ph-d{background:linear-gradient(135deg,#1d4f7a,#b08a5c 55%,#324b6a)}
.tile{background:linear-gradient(135deg,var(--teal-a),var(--teal-b));display:flex;align-items:center;justify-content:center;font-size:7px;font-weight:600}
.pct{position:absolute;top:3px;right:4px;font-size:6.5px;font-weight:700}
.tick{position:absolute;left:50%;top:50%;width:20px;height:20px;margin:-10px 0 0 -10px;border:1.2px solid #fff;border-radius:50%}
.tick:after{content:"";position:absolute;left:6px;top:4px;width:5px;height:8px;border-right:1.4px solid #fff;border-bottom:1.4px solid #fff;transform:rotate(40deg)}
.player .track{position:absolute;top:20px;left:8px;right:8px;border-top:.8px solid #fff}
.player .knob{position:absolute;top:17px;width:6px;height:6px;border-radius:50%;background:#fff}
.player .tm{position:absolute;top:25px;font-size:3px}
.player .btn{position:absolute;left:50%;bottom:8px;width:16px;height:16px;margin-left:-8px;border:1px solid #fff;border-radius:50%}
.acts{position:absolute;top:102px;left:0;right:0;display:flex;gap:10px;font-size:4.5px;align-items:center}
.acts .more{margin-left:auto;color:var(--accent)}
.fab{position:absolute;right:12px;top:281px;width:28px;height:28px;border-radius:50%;background:linear-gradient(135deg,var(--teal-a),var(--teal-b));color:#fff;font-size:18px;line-height:26px;text-align:center;box-shadow:0 2px 6px rgba(0,0,0,.2);font-weight:300}
/* forms */
.label{position:absolute;left:10px;font-size:6px;font-weight:600}
.label .lite{font-weight:400;color:var(--muted);font-size:4px}
.edit{position:absolute;right:10px;font-size:5.5px;color:var(--accent)}
.chips{position:absolute;left:10px;display:flex;gap:4px}
.chip{font-size:4.2px;color:var(--accent);border:.6px solid var(--accent);border-radius:5px;padding:1px 4px;display:flex;align-items:center;gap:3px}
.chip i{display:inline-block;width:5px;height:5px;border-radius:50%;background:var(--accent)}
.rule{position:absolute;left:0;right:0;border-top:.6px solid var(--line)}
.box{position:absolute;left:10px;right:10px;border:.6px solid var(--line);background:#fff;font-size:5px;color:#c3c8cc;padding:7px 5px}
.hint{position:absolute;right:10px;font-size:4px;color:var(--muted)}
.select{position:absolute;left:10px;right:10px;height:16px;border:.6px solid var(--line);font-size:5px;padding:0 6px;display:flex;align-items:center;justify-content:space-between}
.select:after{content:"";border:2px solid transparent;border-top-color:var(--ink)}
.upload{position:absolute;width:77px;height:73px;border:.6px solid var(--line);font-size:4px;color:#c3c8cc;text-align:center}
.upload .ic{margin:16px auto 6px;width:24px;height:18px;border:1px solid #dde2e5;border-radius:2px}
.mic{margin:18px auto 6px;width:8px;height:16px;border:1px solid var(--accent);border-radius:5px}
.radio{position:absolute;display:flex;align-items:center;gap:4px;font-size:5px}
.radio i{width:7px;height:7px;border-radius:50%;border:.6px solid #c9ced2}
.radio.on i{border:2px solid var(--accent)}
.slider{position:absolute;left:10px;right:10px;border-top:1px solid var(--line)}
.slider b{position:absolute;left:0;top:-1px;width:55%;border-top:1.5px solid var(--accent)}
.slider em{position:absolute;left:55%;top:-3.5px;width:6px;height:6px;border-radius:50%;background:#fff;box-shadow:0 0 2px rgba(0,0,0,.3)}
.km{position:absolute;right:10px;font-size:4.5px;color:var(--accent)}
.chev{position:absolute;right:10px;width:4px;height:4px;border-right:.8px solid var(--ink);border-bottom:.8px solid var(--ink)}
/* topics */
.search{position:absolute;left:10px;right:10px;height:15px;border:.6px solid var(--line);font-size:5px;color:#b8bec3;display:flex;align-items:center;gap:5px;padding-left:6px}
.search i{width:6px;height:6px;border:1px solid var(--accent);border-radius:50%}
.topic{position:absolute;width:40px;text-align:center;font-size:4.5px;color:#555}
.ring{margin:0 auto 3px;width:24px;height:24px;border-radius:50%;border:.6px solid #eceff1;position:relative}
.ring:after{content:"";position:absolute;left:7px;top:7px;width:9px;height:9px;border:.7px solid #c9ced2;border-radius:2px}
.topic.on{color:var(--accent)}
.topic.on .ring{border:1.3px solid var(--accent);background:#fff}
.topic.on .ring:after{border-color:var(--accent)}
/* menu */
.menu{background:linear-gradient(180deg,var(--teal-a),var(--teal-b));color:#fff}
.menu-item{position:absolute;left:12px;display:flex;align-items:center;gap:8px;font-size:6.5px}
.menu-item i{width:8px;height:8px;border:.8px solid #fff;border-radius:2px}
.menu-item.on{background:rgba(255,255,255,.22);padding:3px 8px 3px 4px;border-radius:8px;left:5px}
/* rating */
.rate{position:absolute;left:5px;right:5px;color:#fff;padding:5px 6px;font-size:5px}
.rate .big{position:absolute;left:6px;bottom:4px;font-size:11px;font-weight:700;letter-spacing:.3px}
.rate .cols{display:flex;gap:0}
.rate .cols div{flex:1;line-height:1.7}
.rate .h{font-size:4.5px;font-weight:600}
/* modal */
.dim{position:absolute;left:0;right:0;top:0;bottom:0;background:rgba(60,60,60,.55)}
.modal{position:absolute;left:9px;right:11px;top:75px;height:112px;background:#fff;padding:10px 13px}
.btn-fill{background:var(--accent);color:#fff;text-align:center;font-weight:600}
/* notifications */
.note{position:absolute;left:10px;right:10px;font-size:5.5px}
.note .avatar{position:absolute;left:0;top:0;width:16px;height:16px}
.note p{margin-left:24px;line-height:1.4}
.note .when{position:absolute;right:0;font-size:4px;color:#b5bbc0}
</style>
</head>
<body>

<!-- Row 1 -->
<section class="screen menu" style="left:32px;top:54px">
  <div class="abs" style="left:11px;top:42px;width:38px;height:38px;border-radius:50%;border:2px solid #fff;background:linear-gradient(135deg,#7a4a33,#d7a07a)" role="img" aria-label="Profile portrait"></div>
  <div class="abs" style="left:11px;top:86px;font-size:8px;font-weight:600">Jalen Ortega</div>
  <div class="abs" style="left:11px;top:100px;font-size:4.5px;opacity:.9">jalen@example.com</div>
  <div class="menu-item" style="top:145px"><i></i>Home</div>
  <div class="menu-item on" style="top:166px"><i></i>My Profile</div>
  <div class="menu-item" style="top:191px"><i></i>My Activities</div>
  <div class="menu-item" style="top:215px"><i></i>Notification</div>
  <div class="menu-item" style="top:238px"><i></i>Contact Us</div>
  <div class="abs" style="left:0;right:0;top:292px;border-top:.6px solid rgba(255,255,255,.4)"></div>
  <div class="abs" style="left:0;right:0;top:302px;text-align:center;font-size:6.5px">Logout</div>
  <div class="abs" style="left:115px;top:40px;width:70px;height:212px;background:#fff;box-shadow:-3px 3px 8px rgba(0,0,0,.2)">
    <div style="height:20px;background:linear-gradient(90deg,var(--teal-a),var(--teal-b))"></div>
    <div style="position:absolute;left:6px;top:29px;font-size:3px;color:#555">Janelle Ashby</div>
    <div style="position:absolute;left:6px;top:38px;font-size:3px;color:#555">Who is your favourite music</div>
    <div style="position:absolute;left:6px;top:45px;width:52px;height:39px;display:flex;gap:3px"><div class="ph-a" style="flex:1" role="img" aria-label="Guitarist on stage"></div><div class="ph-b" style="flex:1" role="img" aria-label="Guitarist portrait"></div></div>
    <div style="position:absolute;left:6px;top:114px;font-size:3px;color:#555">Who is a better actor?</div>
    <div style="position:absolute;left:6px;top:122px;width:52px;height:42px;display:flex;gap:3px"><div class="ph-c" style="flex:1" role="img" aria-label="Actor portrait"></div><div class="ph-d" style="flex:1" role="img" aria-label="Actor portrait"></div></div>
    <div style="position:absolute;left:6px;top:200px;font-size:3px;color:#555">Choose the best one here?</div>
  </div>
</section>

<section class="screen" style="left:271px;top:54px">
  <div class="bar"><div class="status"><span>••••• ≈</span><span>9:41 AM</span><span>100%<i class="batt"></i></span></div>
    <div class="nav"><span class="burger"></span><span class="title brand">QUERO</span><span class="nav-icons"><span>▽</span><span>○</span></span></div></div>
  <div class="post" style="top:40px">
    <div class="who"><span class="avatar" role="img" aria-label="User avatar"></span>Janelle Ashby <span class="time">3:45pm</span><span class="ago">1 day ago</span></div>
    <div class="q">Who is your favourite music artist?<span class="votes">15 Votes</span></div>
    <div class="pics"><div class="pic ph-a" role="img" aria-label="Guitarist playing on stage"><span class="cap">Dane Holloway</span></div><div class="pic ph-b" role="img" aria-label="Guitarist with double-neck guitar"><span class="cap">Jory Pace</span></div></div>
    <div class="acts"><span>⋖ Share</span><span>▷ Report</span><span class="more">View More</span></div>
  </div>
  <div class="post" style="top:165px">
    <div class="who"><span class="avatar" role="img" aria-label="User avatar"></span>Ronan Fisk <span class="time">3:45pm</span><span class="ago">2 day ago</span></div>
    <div class="q">Who is a better actor?<span class="votes">33 Votes</span></div>
    <div class="pics"><div class="pic ph-c" role="img" aria-label="Actor portrait"><span class="cap">Jonas Deller</span></div><div class="pic ph-d" role="img" aria-label="Actor portrait"><span class="cap">Crispin Vale</span></div></div>
    <div class="acts"><span>⋖ Share</span><span>▷ Report</span><span class="more">View More</span></div>
  </div>
  <div class="post" style="top:289px">
    <div class="who"><span class="avatar" role="img" aria-label="User avatar"></span>Tyson Farrow <span class="time">2:00pm</span></div>
    <div class="q">Choose the best one here?<span class="votes">11 Votes</span></div>
  </div>
  <div class="fab">+</div>
</section>

<section class="screen" style="left:510px;top:54px">
  <div class="bar"><div class="status"><span>••••• ≈</span><span>9:41 AM</span><span>100%<i class="batt"></i></span></div>
    <div class="nav"><span class="burger"></span><span class="title brand">QUERO</span><span class="nav-icons"><span>▽</span><span>○</span></span></div></div>
  <div class="post" style="top:40px">
    <div class="who"><span class="avatar" role="img" aria-label="User avatar"></span>Janelle Ashby <span class="time">3:45pm</span><span class="ago">1 day ago</span></div>
    <div class="q">Who is your favourite music artist?<span class="votes">16 Votes</span></div>
    <div class="pics"><div class="pic tile">Dane Holloway</div><div class="pic tile">Jory Pace</div></div>
    <div class="acts"><span>⋖ Share</span><span>▷ Report</span><span class="more">View More</span></div>
  </div>
  <div class="post" style="top:165px">
    <div class="who"><span class="avatar" role="img" aria-label="User avatar"></span>Ronan Fisk <span class="time">3:45pm</span><span class="ago">2 day ago</span></div>
    <div class="q">Who is a better actor?<span class="votes">33 Votes</span></div>
    <div class="pics"><div class="pic ph-c" role="img" aria-label="Actor portrait"><span class="pct">30%</span><span class="cap">Jonas Deller</span></div><div class="pic ph-d" style="filter:brightness(.6)" role="img" aria-label="Actor portrait, selected"><span class="pct">70%</span><span class="tick"></span><span class="cap">Crispin Vale</span></div></div>
    <div class="acts"><span>⋖ Share</span><span>▷ Report</span><span class="more">View More</span></div>
  </div>
  <div class="post" style="top:289px">
    <div class="who"><span class="avatar" role="img" aria-label="User avatar"></span>Tyson Farrow <span class="time">2:00pm</span></div>
    <div class="q">Choose the best one here?<span class="votes">11 Votes</span></div>
  </div>
  <div class="fab">+</div>
</section>

<section class="screen" style="left:749px;top:54px">
  <div class="bar"><div class="status"><span>••••• ≈</span><span>9:41 AM</span><span>100%<i class="batt"></i></span></div>
    <div class="nav"><span class="burger"></span><span class="title brand">QUERO</span><span class="nav-icons"><span>▽</span><span>○</span></span></div></div>
  <div class="post" style="top:40px">
    <div class="who"><span class="avatar" role="img" aria-label="User avatar"></span>Janelle Ashby <span class="time">3:45pm</span><span class="ago">1 day ago</span></div>
    <div class="q">Who is your favourite music artist?<span class="votes">15 Votes</span></div>
    <div class="pics">
      <div class="pic tile player"><span class="track"></span><span class="knob" style="left:24px"></span><span class="tm" style="left:8px">0:12</span><span class="tm" style="right:8px">1:30</span><span class="btn"></span></div>
      <div class="pic tile player"><span class="track"></span><span class="knob" style="left:10px"></span><span class="tm" style="left:8px">0:00</span><span class="tm" style="right:8px">1:30</span><span class="btn"></span></div>
    </div>
    <div class="acts"><span>⋖ Share</span><span>▷ Report</span><span class="more">View More</span></div>
  </div>
  <div class="post" style="top:165px">
    <div class="who"><span class="avatar" role="img" aria-label="User avatar"></span>Ronan Fisk <span class="time">3:45pm</span><span class="ago">2 day ago</span></div>
    <div class="q">Who is a better actor?<span class="votes">33 Votes</span></div>
    <div class="pics"><div class="pic ph-c" role="img" aria-label="Actor portrait"><span class="pct">30%</span><span class="cap">Jonas Deller</span></div><div class="pic ph-d" style="filter:brightness(.6)" role="img" aria-label="Actor portrait, selected"><span class="pct">70%</span><span class="tick"></span><span class="cap">Crispin Vale</span></div></div>
    <div class="acts"><span>⋖ Share</span><span>▷ Report</span><span class="more">View More</span></div>
  </div>
  <div class="post" style="top:289px">
    <div class="who"><span class="avatar" role="img" aria-label="User avatar"></span>Tyson Farrow <span class="time">2:00pm</span></div>
    <div class="q">Choose the best one here?<span class="votes">11 Votes</span></div>
  </div>
  <div class="fab">+</div>
</section>

<section class="screen" style="left:987px;top:54px">
  <div class="bar"><div class="status"><span>••••• ≈</span><span>9:41 AM</span><span>100%<i class="batt"></i></span></div>
    <div class="nav"><span class="back">←</span><span class="title">Post a Question</span><span>Next</span></div></div>
  <div class="search" style="top:44px"><i></i>Search Topics or Interest</div>
  <div class="label" style="top:76px">What is your question about?</div>
  <div class="topic on" style="left:4px;top:98px"><div class="ring"></div>Science</div>
  <div class="topic" style="left:48px;top:98px"><div class="ring"></div>Technology</div>
  <div class="topic" style="left:91px;top:98px"><div class="ring"></div>Gadgets</div>
  <div class="topic" style="left:134px;top:98px"><div class="ring"></div>Health</div>
  <div class="topic" style="left:4px;top:150px"><div class="ring"></div>Fashion</div>
  <div class="topic" style="left:48px;top:150px"><div class="ring"></div>Travel</div>
  <div class="topic on" style="left:91px;top:150px"><div class="ring"></div>Religion</div>
  <div class="topic" style="left:134px;top:150px"><div class="ring"></div>History</div>
  <div class="topic" style="left:4px;top:203px"><div class="ring"></div>Languages</div>
  <div class="topic on" style="left:48px;top:203px"><div class="ring"></div>Education</div>
  <div class="topic" style="left:91px;top:203px"><div class="ring"></div>Business</div>
  <div class="topic" style="left:134px;top:203px"><div class="ring"></div>Finance</div>
  <div class="topic" style="left:4px;top:256px"><div class="ring"></div>My Country</div>
  <div class="topic" style="left:48px;top:256px"><div class="ring"></div>My City</div>
</section>

<!-- Row 2 -->
<section class="screen" style="left:32px;top:440px">
  <div class="bar"><div class="status"><span>••••• ≈</span><span>9:41 AM</span><span>100%<i class="batt"></i></span></div>
    <div class="nav"><span class="back">←</span><span class="title">Post a Question</span><span>Next</span></div></div>
  <div class="label" style="top:43px">Your Question is about</div><div class="edit" style="top:43px">Edit</div>
  <div class="chips" style="top:62px"><span class="chip">Science<i></i></span><span class="chip">Religion<i></i></span><span class="chip">Education<i></i></span></div>
  <div class="rule" style="top:78px"></div>
  <div class="label" style="top:86px">What is your question?</div>
  <div class="box" style="top:105px;height:58px">Write text here....</div>
  <div class="hint" style="top:169px">30 Words Max</div>
  <div class="rule" style="top:180px"></div>
  <div class="label" style="top:188px">What are the options?</div>
  <div class="select" style="top:206px">Text</div>
  <div class="box" style="top:234px;height:33px">Option 1 here....</div>
  <div class="box" style="top:275px;height:33px">Option 2 here....</div>
</section>

<section class="screen" style="left:271px;top:440px">
  <div class="bar"><div class="status"><span>••••• ≈</span><span>9:41 AM</span><span>100%<i class="batt"></i></span></div>
    <div class="nav"><span class="back">←</span><span class="title">Post a Question</span><span>Next</span></div></div>
  <div class="label" style="top:43px">Your Question is about</div><div class="edit" style="top:43px">Edit</div>
  <div class="chips" style="top:62px"><span class="chip">Science<i></i></span><span class="chip">Religion<i></i></span><span class="chip">Education<i></i></span></div>
  <div class="rule" style="top:78px"></div>
  <div class="label" style="top:86px">What is your question?</div>
  <div class="box" style="top:105px;height:58px">Write text here....</div>
  <div class="hint" style="top:169px">30 Words Max</div>
  <div class="rule" style="top:180px"></div>
  <div class="label" style="top:188px">What are the options?</div>
  <div class="select" style="top:206px">Images</div>
  <div class="upload" style="left:10px;top:234px"><div class="ic"></div>Tap to Upload<br>photo</div>
  <div class="upload" style="left:93px;top:234px"><div class="ic"></div>Tap to Upload<br>photo</div>
</section>

<section class="screen" style="left:510px;top:440px">
  <div class="bar"><div class="status"><span>••••• ≈</span><span>9:41 AM</span><span>100%<i class="batt"></i></span></div>
    <div class="nav"><span class="back">←</span><span class="title">Post a Question</span><span>Next</span></div></div>
  <div class="label" style="top:43px">Your Question is about</div><div class="edit" style="top:43px">Edit</div>
  <div class="chips" style="top:62px"><span class="chip">Science<i></i></span><span class="chip">Religion<i></i></span><span class="chip">Education<i></i></span></div>
  <div class="rule" style="top:78px"></div>
  <div class="label" style="top:86px">What is your question?</div>
  <div class="box" style="top:105px;height:58px">Write text here....</div>
  <div class="hint" style="top:169px">30 Words Max</div>
  <div class="rule" style="top:180px"></div>
  <div class="label" style="top:188px">What are the options?</div>
  <div class="select" style="top:206px">Images</div>
  <div class="upload" style="left:10px;top:234px;color:var(--accent)"><div class="mic"></div>0:10</div>
  <div class="upload" style="left:93px;top:234px"><div class="mic" style="border-color:#dde2e5"></div>Hold to Record</div>
</section>

<section class="screen" style="left:749px;top:440px">
  <div class="bar"><div class="status"><span>••••• ≈</span><span>9:41 AM</span><span>100%<i class="batt"></i></span></div>
    <div class="nav"><span>Cancel</span><span class="title">Filter</span><span>Apply</span></div></div>
  <div class="label" style="top:43px">Interests</div><div class="chev" style="top:47px;transform:rotate(-135deg)"></div>
  <div class="chips" style="top:62px"><span class="chip">Science<i></i></span><span class="chip">Religion<i></i></span><span class="chip">Education<i></i></span></div>
  <div class="rule" style="top:80px"></div>
  <div class="label" style="top:90px">Questions</div>
  <div class="radio on" style="left:10px;top:109px"><i></i>My Questions</div>
  <div class="radio" style="left:80px;top:109px"><i></i>All Questions</div>
  <div class="rule" style="top:127px"></div>
  <div class="label" style="top:143px">Location <span class="lite">(Limit search to)</span></div>
  <div class="slider" style="top:164px"><b></b><em></em></div>
  <div class="km" style="top:171px">46km</div>
  <div class="rule" style="top:187px"></div>
  <div class="label" style="top:199px">Sort by</div>
  <div class="radio on" style="left:10px;top:218px"><i></i>Newest</div>
  <div class="radio" style="left:10px;top:240px"><i></i>Popular</div>
  <div class="radio" style="left:10px;top:265px"><i></i>Trending</div>
</section>

<section class="screen" style="left:987px;top:440px">
  <div class="bar"><div class="status"><span>••••• ≈</span><span>9:41 AM</span><span>100%<i class="batt"></i></span></div>
    <div class="nav"><span>Cancel</span><span class="title">Filter</span><span>Apply</span></div></div>
  <div class="label" style="top:43px">Interests</div><div class="chev" style="top:44px;transform:rotate(45deg)"></div>
  <div class="rule" style="top:61px"></div>
  <div class="label" style="top:71px">Questions</div>
  <div class="radio on" style="left:10px;top:90px"><i></i>My Questions</div>
  <div class="radio" style="left:80px;top:90px"><i></i>All Questions</div>
  <div class="rule" style="top:111px"></div>
  <div class="label" style="top:124px">Location <span class="lite">(Limit search to)</span></div>
  <div class="slider" style="top:145px"><b></b><em></em></div>
  <div class="km" style="top:152px">46km</div>
  <div class="rule" style="top:167px"></div>
  <div class="label" style="top:180px">Sort by</div>
  <div class="radio on" style="left:10px;top:198px"><i></i>Newest</div>
  <div class="radio" style="left:10px;top:220px"><i></i>Popular</div>
  <div class="radio" style="left:10px;top:246px"><i></i>Trending</div>
</section>

<!-- Row 3 -->
<section class="screen" style="left:32px;top:825px">
  <div class="bar"><div class="status"><span>••••• ≈</span><span>9:41 AM</span><span>100%<i class="batt"></i></span></div>
    <div class="nav"><span style="font-size:10px">⊕</span><span class="title brand">QUERO</span><span>Done</span></div></div>
  <div class="search" style="top:44px"><i></i>Search Topics or Interest</div>
  <div class="label" style="top:75px">Select topic or interest?</div>
  <div class="topic on" style="left:4px;top:99px"><div class="ring"></div>Science</div>
  <div class="topic" style="left:48px;top:99px"><div class="ring"></div>Technology</div>
  <div class="topic" style="left:91px;top:99px"><div class="ring"></div>Gadgets</div>
  <div class="topic" style="left:134px;top:99px"><div class="ring"></div>Health</div>
  <div class="topic" style="left:4px;top:152px"><div class="ring"></div>Fashion</div>
  <div class="topic" style="left:48px;top:152px"><div class="ring"></div>Travel</div>
  <div class="topic on" style="left:91px;top:152px"><div class="ring"></div>Religion</div>
  <div class="topic" style="left:134px;top:152px"><div class="ring"></div>History</div>
  <div class="topic" style="left:4px;top:204px"><div class="ring"></div>Languages</div>
  <div class="topic on" style="left:48px;top:204px"><div class="ring"></div>Education</div>
  <div class="topic" style="left:91px;top:204px"><div class="ring"></div>Business</div>
  <div class="topic" style="left:134px;top:204px"><div class="ring"></div>Finance</div>
  <div class="topic" style="left:4px;top:256px"><div class="ring"></div>My Country</div>
  <div class="topic" style="left:48px;top:256px"><div class="ring"></div>My City</div>
</section>

<section class="screen" style="left:271px;top:825px">
  <div class="bar"><div class="status"><span>••••• ≈</span><span>9:41 AM</span><span>100%<i class="batt"></i></span></div>
    <div class="nav"><span style="font-size:10px">⊕</span><span class="title brand">QUERO</span><span>Done</span></div></div>
  <div class="search" style="top:44px"><i></i>Search Topics or Interest</div>
  <div class="topic" style="left:4px;top:204px"><div class="ring"></div>Languages</div>
  <div class="topic on" style="left:48px;top:204px"><div class="ring"></div>Education</div>
  <div class="topic" style="left:91px;top:204px"><div class="ring"></div>Business</div>
  <div class="topic" style="left:134px;top:204px"><div class="ring"></div>Finance</div>
  <div class="topic" style="left:4px;top:256px"><div class="ring"></div>My Country</div>
  <div class="topic" style="left:48px;top:256px"><div class="ring"></div>My City</div>
  <div class="dim"></div>
  <div class="modal">
    <div style="position:absolute;right:6px;top:3px;font-size:8px">×</div>
    <div style="font-size:7px;margin-top:6px">Enter new interest</div>
    <div style="margin-top:7px;height:14px;border:.6px solid var(--line);font-size:4.5px;color:#bbb;padding:3px 5px">Type here...</div>
    <div style="display:flex;justify-content:space-between;font-size:4.5px;margin-top:4px"><span style="color:#bbb">+ Add Subtopic</span><span style="color:var(--accent)">Add More</span></div>
    <div class="btn-fill" style="margin-top:17px;height:15px;line-height:15px;font-size:6px">Submit</div>
  </div>
</section>

<section class="screen" style="left:510px;top:825px">
  <div class="bar"><div class="status"><span>••••• ≈</span><span>9:41 AM</span><span>100%<i class="batt"></i></span></div>
    <div class="nav"><span class="back">←</span><span class="title brand">QUERO</span><span></span></div></div>
  <div class="rate" style="top:37px;height:82px;background:linear-gradient(180deg,#74e0d5,#27b0b6)" role="img" aria-label="Teal mountain landscape backdrop">
    <div style="margin-top:12px;line-height:1.8;opacity:.9">Option 1 - 455<br>Option 2 - 231</div><div class="big">OVERALL RATING</div></div>
  <div class="rate" style="top:124px;height:82px;background:linear-gradient(180deg,#e9d6a8,#b0a055 70%,#6f7a3a)" role="img" aria-label="Golden hills landscape backdrop">
    <div class="cols"><div><span class="h">MALE</span><br>Option 1 - 455<br>Option 2 - 231</div><div><span class="h">FEMALE</span><br>Option 1 - 455<br>Option 2 - 231</div><div><span class="h">OTHERS</span><br>Option 1 - 455<br>Option 2 - 231</div></div><div class="big">GENDER</div></div>
  <div class="rate" style="top:211px;height:82px;background:linear-gradient(180deg,#f3b6a0,#e47a62 65%,#b3423a)" role="img" aria-label="Coral mountain landscape backdrop">
    <div class="cols"><div><span class="h">18 - 30</span><br>Option 1 - 455<br>Option 2 - 231</div><div><span class="h">30 - 45</span><br>Option 1 - 455<br>Option 2 - 231</div><div><span class="h">45 - 60+</span><br>Option 1 - 455<br>Option 2 - 231</div></div><div class="big">AGE</div></div>
  <div class="rate" style="top:298px;height:30px;background:linear-gradient(180deg,#e8c6ef,#c5a2e3)" role="img" aria-label="Lilac landscape backdrop">
    <div class="cols"><div class="h">MALE</div><div class="h">FEMALE</div><div class="h">OTHERS</div></div></div>
</section>

<section class="screen" style="left:749px;top:825px">
  <div class="bar"><div class="status"><span>••••• ≈</span><span>9:41 AM</span><span>100%<i class="batt"></i></span></div>
    <div class="nav"><span class="back">←</span><span class="title">Contact Us</span><span></span></div></div>
  <div class="abs" style="left:0;right:0;top:32px;height:94px;background:radial-gradient(circle at 50% 45%,#bfe9f7 0 28%,#2aa7e0 29%)" role="img" aria-label="Illustrated fishbowl with a goldfish"></div>
  <div class="abs" style="left:22px;right:22px;top:114px;height:182px;background:#fff;box-shadow:0 1px 6px rgba(0,0,0,.12);padding:12px 10px">
    <div style="font-size:8px">Get in touch</div>
    <div style="font-size:4.5px;margin-top:12px">Name</div>
    <div style="font-size:5px;color:#ccc;border-bottom:.6px solid var(--line);padding:2px 0">Enter name here</div>
    <div style="font-size:4.5px;margin-top:11px">Email</div>
    <div style="font-size:5px;color:#ccc;border-bottom:.6px solid var(--line);padding:2px 0">Enter email here</div>
    <div style="font-size:4.5px;margin-top:11px">Message</div>
    <div style="font-size:5px;color:#ccc;border:.6px solid var(--line);height:52px;margin-top:3px;padding:3px">Enter message here</div>
  </div>
  <div class="abs btn-fill" style="left:67px;width:48px;top:279px;height:16px;line-height:16px;border-radius:8px;font-size:6px;box-shadow:0 1px 4px rgba(0,0,0,.2)">Submit</div>
</section>

<section class="screen" style="left:987px;top:825px">
  <div class="bar"><div class="status"><span>••••• ≈</span><span>9:41 AM</span><span>100%<i class="batt"></i></span></div>
    <div class="nav"><span class="back">←</span><span class="title">Notifications</span><span></span></div></div>
  <div class="note" style="top:44px"><span class="avatar" role="img" aria-label="User avatar"></span><p><b style="font-weight:600">Jonah Gustafson</b> posted a question in the science category</p><span class="when" style="top:20px">Today at 4:30</span></div>
  <div class="rule" style="top:72px;left:10px;right:10px"></div>
  <div class="note" style="top:84px"><span class="avatar" role="img" aria-label="User avatar"></span><p><b style="font-weight:600">Sera Janes</b> answered to your question</p><span class="when" style="top:16px">Yesterday</span></div>
  <div class="rule" style="top:111px;left:10px;right:10px"></div>
  <div class="note" style="top:123px"><span class="avatar" role="img" aria-label="User avatar"></span><p><b style="font-weight:600">Selma Jonsen</b> shared your post</p><span class="when" style="top:16px">1 day ago</span></div>
  <div class="rule" style="top:150px;left:10px;right:10px"></div>
  <div class="note" style="top:162px"><span class="avatar" role="img" aria-label="User avatar"></span><p>Your new topic <span style="color:var(--accent)">Glamour</span> has been added</p><span class="when" style="top:16px">2 days ago</span></div>
  <div class="rule" style="top:189px;left:10px;right:10px"></div>
  <div class="note" style="top:201px"><span class="avatar" role="img" aria-label="User avatar"></span><p><b style="font-weight:600">Rowan Smythe</b> answered your question</p><span class="when" style="top:16px">a week ago</span></div>
  <div class="rule" style="top:228px;left:10px;right:10px"></div>
  <div class="note" style="top:241px"><span class="avatar" role="img" aria-label="User avatar"></span><p><b style="font-weight:600">Lidia Lane</b> shared your post</p><span class="when" style="top:16px">a month ago</span></div>
</section>

</body>
</html>
```